Environmental Consultancy needs new professional Word Template for reporting

A professional looking word template that we can use for all of our reporting.

Word template needs:
- a full scale title page that we can include a different photograph on for each new project, our company logo, title, date, and client details
- Include four layered Headings, table of contents page.
- Each page (except title page) needs to be numbered, with the title of the report at the bottom of the page.
- each page needs our company logo at the top.
- Prefer it to be using similar colours to what we are currently using. Though open to new colours if you come up with something that suits what we do.

Our business is an environment/ecological consultancy and we provide a number of field and reporting based services to mining companies, government agencies, commercial developers, landholders, tourism operators etc. Some of the work we do includes:
- vegetation surveys and reporting
- fauna trapping surveys, and reporting
- water quality and aquatic ecosystem monitoring and reporting
- fish and macroinvertebrate surveys
- seagrass and coral surveys
- environmental impact statements
- environmental offsets
- rehabilitation design and monitoring
- monitoring design programs
- ecological constraints surveys.

I have attached our company logo, a copy of our current title page, and an extract of our current report style (has been greatly reduced and with client information removed). I would like sometime similar to this report style please.

Low design quality

Target Market(s)

Client and Government approval agencies

Industry/Entity Type

Environmental Consultant

Font styles to use
Sans Serif

Colors
faa54b
9bcb3c
00a990
83c9e6
85acd3

Requirements
Must have
• Word template needs:

```html
<!DOCTYPE html>
<html lang="en">
<head>
<meta charset="utf-8">
<title>Fernway Ecology – Report Template</title>
<link rel="stylesheet" href="https://fonts.googleapis.com/css2?family=Kalam:wght@700&family=Source+Sans+3:ital,wght@0,400;0,600;0,700;1,400&display=swap">
<style>
  :root {
    --canvas: #e3dad0;
    --paper: #ffffff;
    --leaf-dark: #1f3326;
    --leaf-mid: #3d5e45;
    --forest: #3f6b3a;
    --rust: #b8693d;
    --rust-soft: #c98a5d;
    --sand: #d9b596;
    --cream: #f8e4d4;
    --row-tint: #f6ece4;
    --sage: #d6e2cc;
    --ink: #3a3a3a;
    --muted: #6b6b6b;
  }
  * { box-sizing: border-box; margin: 0; padding: 0; }
  html, body { width: 1200px; height: 3000px; overflow: hidden; }
  body {
    background: var(--canvas);
    position: relative;
    font-family: "Source Sans 3", Arial, sans-serif;
    color: var(--ink);
  }
  .page {
    position: absolute;
    width: 540px;
    height: 764px;
    background: var(--paper);
    box-shadow: 0 6px 18px rgba(60, 45, 30, 0.18);
    overflow: hidden;
  }
  .page--cover { left: 70px; top: 80px; }
  .page--contents { left: 600px; top: 360px; }
  .page--body-odd { left: 70px; top: 900px; }
  .page--body-even { left: 600px; top: 1180px; }
  .page--back { left: 70px; top: 1720px; }

  .full-art { position: absolute; inset: 0; width: 100%; height: 100%; }

  .brand {
    font-family: "Source Sans 3", Arial, sans-serif;
    font-weight: 600;
    color: var(--rust);
    display: inline-flex;
    align-items: center;
    gap: 6px;
    white-space: nowrap;
  }
  .brand__dot { width: 8px; height: 8px; border-radius: 50%; background: var(--forest); }

  .cover-brand { position: absolute; top: 44px; right: 34px; font-size: 24px; }
  .cover-title {
    position: absolute; left: 48px; top: 640px;
    font-family: "Kalam", cursive;
    font-weight: 700;
    color: var(--forest);
    font-size: 50px;
    line-height: 1;
  }
  .cover-subtitle {
    position: absolute; left: 50px; top: 708px;
    font-family: "Kalam", cursive;
    font-weight: 700;
    color: var(--forest);
    font-size: 22px;
  }

  /* running header */
  .running-head {
    position: absolute; top: 32px; left: 48px; right: 36px;
    display: flex; align-items: center; gap: 8px;
  }
  .running-head .brand { font-size: 15px; }
  .running-head__rule { flex: 1; height: 2px; background: var(--forest); margin-top: 10px; }

  /* running footer */
  .running-foot {
    position: absolute; bottom: 34px; left: 48px; right: 40px;
    display: flex; align-items: center; gap: 10px;
    font-size: 9px; text-transform: uppercase; color: var(--muted);
  }
  .running-foot__rule { width: 160px; height: 2px; background: var(--rust); }
  .running-foot__spacer { flex: 1; }
  .page-number {
    display: inline-flex; align-items: center; justify-content: center;
    width: 16px; height: 16px; background: var(--rust); color: #fff;
    font-size: 9px; font-weight: 600;
  }

  .page-body { position: absolute; top: 78px; left: 52px; right: 52px; }

  .h1 { font-size: 17px; font-weight: 700; color: var(--rust); margin-bottom: 8px; }
  .h2 { font-size: 14px; font-weight: 400; color: var(--rust); margin: 20px 0 8px; }
  .h3 { font-size: 12.5px; font-weight: 400; color: var(--rust); margin: 20px 0 8px; }
  .h4 { font-size: 12px; font-weight: 400; color: var(--rust); margin: 20px 0 8px; }
  .body-text { font-size: 10px; line-height: 1.35; margin-bottom: 8px; }

  .special-heading {
    font-size: 9.5px; font-weight: 700; color: var(--forest);
    text-transform: uppercase; border-bottom: 1.5px solid var(--forest);
    padding-bottom: 3px; margin: 22px 0 8px;
  }
  .special-text {
    font-size: 10px; line-height: 1.35; font-style: italic;
    color: var(--forest); text-align: justify; margin-bottom: 8px;
  }

  /* contents */
  .contents-title { font-size: 15px; font-weight: 700; color: var(--rust); margin-bottom: 10px; }
  .toc { list-style: none; font-size: 10.5px; }
  .toc li { display: flex; align-items: baseline; margin-bottom: 4px; }
  .toc__num { width: 32px; }
  .toc__label { white-space: nowrap; }
  .toc__leader { flex: 1; border-bottom: 1.5px dotted currentColor; margin: 0 2px; transform: translateY(-3px); }
  .toc__main { color: var(--rust); font-weight: 600; }
  .toc__sub { color: var(--ink); }
  .toc__sub .toc__num { width: 30px; margin-left: 32px; }
  .toc__sub--deep .toc__num { width: 40px; }

  /* table */
  .data-table { width: 100%; border-collapse: collapse; font-size: 9.5px; margin-bottom: 22px; }
  .data-table th {
    background: var(--rust); color: #fff; text-align: left;
    font-weight: 600; padding: 3px 6px;
  }
  .data-table td { padding: 3px 6px; }
  .data-table tr:nth-child(even) td { background: var(--row-tint); }

  .figure { margin: 10px 0 22px; }
  .figure__art { display: block; width: 100%; height: 236px; }
  .figure__caption {
    background: var(--sage); font-size: 7.5px; color: var(--muted);
    text-align: center; padding: 2px 0;
  }

  .bullets { list-style: none; font-size: 10px; margin-top: 8px; }
  .bullets li { margin-bottom: 3px; padding-left: 22px; position: relative; }
  .bullets li::before { content: "»"; position: absolute; left: 2px; }
  .bullets .bullets__nested { padding-left: 40px; }
  .bullets .bullets__nested::before { content: "•"; left: 28px; }

  /* back cover panel */
  .back-panel {
    position: absolute; left: 160px; top: 520px; width: 270px; height: 224px;
    background: rgba(245, 243, 240, 0.96);
    padding: 22px 20px 0;
  }
  .back-panel .brand { font-size: 22px; margin-bottom: 12px; }
  .contact-list { list-style: none; font-size: 11px; line-height: 1.45; color: var(--ink); }
  .contact-list li { display: flex; gap: 8px; align-items: flex-start; }
  .contact-list svg { flex: none; margin-top: 3px; }
  .back-panel__band { position: absolute; left: 0; right: 0; bottom: 0; height: 24px; background: var(--sand); }
</style>
</head>
<body>

<!-- Front cover -->
<section class="page page--cover">
  <svg class="full-art" viewBox="0 0 540 764" preserveAspectRatio="none">
    <defs>
      <linearGradient id="leafCover" x1="0" y1="0" x2="1" y2="1">
        <stop offset="0" stop-color="#253b2c"/>
        <stop offset="0.5" stop-color="#3d5e45"/>
        <stop offset="1" stop-color="#1c2d22"/>
      </linearGradient>
    </defs>
    <rect width="540" height="620" fill="url(#leafCover)" role="img" aria-label="Project photograph: close view of dark green leaves with rain drops"/>
    <path d="M290 0 C305 70 360 100 430 100 C480 100 515 88 540 78 V0 Z" fill="#ffffff"/>
    <path d="M0 560 C110 500 200 520 300 480 C400 440 470 470 540 430 V640 H0 Z" fill="#3f6b3a" opacity="0.9"/>
    <path d="M0 580 C90 610 190 570 300 560 C400 550 480 520 540 500 V764 H0 Z" fill="#f8e4d4"/>
    <path d="M0 615 C110 650 220 605 330 595 C430 585 490 575 540 560 V764 H0 Z" fill="#d9b596"/>
  </svg>
  <div class="brand cover-brand"><span class="brand__dot"></span>Fernway Ecology</div>
  <h1 class="cover-title">Main Title Here</h1>
  <p class="cover-subtitle">Subtitle here</p>
</section>

<!-- Contents page -->
<section class="page page--contents">
  <header class="running-head">
    <span class="running-head__rule"></span>
    <span class="brand"><span class="brand__dot"></span>Fernway Ecology</span>
  </header>
  <div class="page-body">
    <h2 class="contents-title">Table of Contents</h2>
    <ul class="toc">
      <li class="toc__main"><span class="toc__num">01.</span><span class="toc__label">Heading 1</span><span class="toc__leader"></span>3</li>
      <li class="toc__sub"><span class="toc__num">1.1.</span><span class="toc__label">Heading 2</span><span class="toc__leader"></span>3</li>
      <li class="toc__sub"><span class="toc__num">1.1.1.</span><span class="toc__label">Heading 3</span><span class="toc__leader"></span>3</li>
      <li class="toc__sub toc__sub--deep"><span class="toc__num">1.1.1.1.</span><span class="toc__label">Heading 4</span><span class="toc__leader"></span>3</li>
      <li class="toc__main"><span class="toc__num">02.</span><span class="toc__label">Tables</span><span class="toc__leader"></span>4</li>
      <li class="toc__main"><span class="toc__num">03.</span><span class="toc__label">Images</span><span class="toc__leader"></span>4</li>
      <li class="toc__main"><span class="toc__num">04.</span><span class="toc__label">Bullets</span><span class="toc__leader"></span>4</li>
    </ul>
  </div>
  <footer class="running-foot">
    <span class="running-foot__rule"></span>
    <span class="running-foot__spacer"></span>
    <span>Title of the report</span>
    <span class="page-number">2</span>
  </footer>
</section>

<!-- Body page 3 -->
<section class="page page--body-odd">
  <header class="running-head">
    <span class="brand"><span class="brand__dot"></span>Fernway Ecology</span>
    <span class="running-head__rule"></span>
  </header>
  <div class="page-body">
    <h2 class="h1">01. Heading 1</h2>
    <p class="body-text">Lorem ipsum dolor sit amet, consectetuer adipiscing elit. Maecenas porttitor congue massa. Fusce posuere, magna sed pulvinar ultricies, purus lectus malesuada libero, sit amet commodo magna eros quis urna.</p>
    <p class="body-text">Nunc viverra imperdiet enim. Fusce est. Vivamus a tellus.</p>

    <h3 class="h2">1.1. Heading 2</h3>
    <p class="body-text">Lorem ipsum dolor sit amet, consectetuer adipiscing elit. Maecenas porttitor congue massa. Fusce posuere, magna sed pulvinar ultricies, purus lectus malesuada libero, sit amet commodo magna eros quis urna.</p>
    <p class="body-text">Nunc viverra imperdiet enim. Fusce est. Vivamus a tellus.</p>

    <h4 class="h3">1.1.1. Heading 3</h4>
    <p class="body-text">Lorem ipsum dolor sit amet, consectetuer adipiscing elit. Maecenas porttitor congue massa. Fusce posuere, magna sed pulvinar ultricies, purus lectus malesuada libero, sit amet commodo magna eros quis urna.</p>
    <p class="body-text">Nunc viverra imperdiet enim. Fusce est. Vivamus a tellus.</p>

    <h5 class="h4">1.1.1.1. Heading 4</h5>
    <p class="body-text">Lorem ipsum dolor sit amet, consectetuer adipiscing elit. Maecenas porttitor congue massa. Fusce posuere, magna sed pulvinar ultricies, purus lectus malesuada libero, sit amet commodo magna eros quis urna.</p>
    <p class="body-text">Nunc viverra imperdiet enim. Fusce est. Vivamus a tellus.</p>

    <h6 class="special-heading">Special heading</h6>
    <p class="special-text">Lorem ipsum dolor sit amet, consectetuer adipiscing elit. Maecenas porttitor congue massa. Fusce posuere, magna sed pulvinar ultricies, purus lectus malesuada libero, sit amet commodo magna eros quis urna. Lorem ipsum dolor sit amet, consectetuer adipiscing elit. Maecenas porttitor congue massa. Fusce posuere, magna sed pulvinar ultricies, purus lectus malesuada libero, sit amet commodo magna eros quis urna.</p>
    <p class="special-text">Lorem ipsum dolor sit amet, consectetuer adipiscing elit. Maecenas porttitor congue massa. Fusce posuere, magna sed pulvinar ultricies, purus lectus malesuada libero, sit amet commodo magna eros quis urna.</p>
    <p class="special-text">Lorem ipsum dolor sit amet, consectetuer adipiscing elit. Maecenas porttitor congue massa. Fusce posuere, magna sed pulvinar ultricies, purus lectus malesuada libero, sit amet commodo magna eros quis urna.</p>
  </div>
  <footer class="running-foot">
    <span class="page-number">3</span>
    <span>Title of the report</span>
    <span class="running-foot__spacer"></span>
    <span class="running-foot__rule"></span>
  </footer>
</section>

<!-- Body page 4 -->
<section class="page page--body-even">
  <header class="running-head">
    <span class="running-head__rule"></span>
    <span class="brand"><span class="brand__dot"></span>Fernway Ecology</span>
  </header>
  <div class="page-body">
    <h2 class="h1">02. Tables</h2>
    <table class="data-table">
      <thead><tr><th>Title</th><th>Title</th><th>Title</th><th>Title</th></tr></thead>
      <tbody>
        <tr><td>00000</td><td>00000</td><td>00000</td><td>00000</td></tr>
        <tr><td>00000</td><td>00000</td><td>00000</td><td>00000</td></tr>
        <tr><td>00000</td><td>00000</td><td>00000</td><td>00000</td></tr>
        <tr><td>00000</td><td>00000</td><td>00000</td><td>00000</td></tr>
        <tr><td>00000</td><td>00000</td><td>00000</td><td>00000</td></tr>
      </tbody>
    </table>

    <h2 class="h1">03. Images</h2>
    <figure class="figure">
      <svg class="figure__art" viewBox="0 0 436 236" preserveAspectRatio="none" role="img" aria-label="Report photograph: dark green leaves with rain drops">
        <defs>
          <linearGradient id="leafFigure" x1="0" y1="0" x2="1" y2="1">
            <stop offset="0" stop-color="#2a4231"/>
            <stop offset="0.55" stop-color="#44664b"/>
            <stop offset="1" stop-color="#1e3024"/>
          </linearGradient>
        </defs>
        <rect width="436" height="236" fill="url(#leafFigure)"/>
      </svg>
      <figcaption class="figure__caption">Figure 1: image details here</figcaption>
    </figure>

    <h2 class="h1">04. Bullets</h2>
    <ul class="bullets">
      <li>Lorem ipsum</li>
      <li class="bullets__nested">Lorem ipsum</li>
      <li>Lorem ipsum</li>
      <li>Lorem ipsum</li>
      <li>Lorem ipsum</li>
    </ul>
  </div>
  <footer class="running-foot">
    <span class="running-foot__rule"></span>
    <span class="running-foot__spacer"></span>
    <span>Title of the report</span>
    <span class="page-number">4</span>
  </footer>
</section>

<!-- Back cover -->
<section class="page page--back">
  <svg class="full-art" viewBox="0 0 540 764" preserveAspectRatio="none" role="img" aria-label="Back cover photograph: dark green leaves with rain drops">
    <defs>
      <linearGradient id="leafBack" x1="1" y1="0" x2="0" y2="1">
        <stop offset="0" stop-color="#2b4432"/>
        <stop offset="0.5" stop-color="#3f6047"/>
        <stop offset="1" stop-color="#1b2b20"/>
      </linearGradient>
    </defs>
    <rect width="540" height="764" fill="url(#leafBack)"/>
  </svg>
  <div class="back-panel">
    <div class="brand"><span class="brand__dot"></span>Fernway Ecology</div>
    <ul class="contact-list">
      <li><svg width="10" height="10" viewBox="0 0 10 10"><circle cx="5" cy="5" r="5" fill="#3f6b3a"/><circle cx="5" cy="5" r="2.6" fill="none" stroke="#fff" stroke-width="1"/></svg>www.fernwayecology.com.au</li>
      <li><svg width="10" height="10" viewBox="0 0 10 10"><circle cx="5" cy="5" r="5" fill="#3f6b3a"/><rect x="2.5" y="3.3" width="5" height="3.4" fill="none" stroke="#fff" stroke-width="0.9"/></svg>mia@fernwayecology.com.au</li>
      <li><svg width="10" height="10" viewBox="0 0 10 10"><circle cx="5" cy="5" r="5" fill="#3f6b3a"/><path d="M3.3 2.8 L4.3 2.8 L4.8 4.1 L4.2 4.6 Q4.8 5.6 5.5 6 L6 5.4 L7.2 5.9 L7.2 6.9 Q4 7.2 3.3 2.8Z" fill="#fff"/></svg>0355 501 234</li>
      <li><svg width="10" height="10" viewBox="0 0 10 10"><circle cx="5" cy="5" r="5" fill="#3f6b3a"/><circle cx="5" cy="4.3" r="1.6" fill="none" stroke="#fff" stroke-width="1"/><path d="M5 6 L5 7.6" stroke="#fff" stroke-width="1"/></svg><span>Queensland Office<br>PO Box 12, Riverton QLD 4810</span></li>
      <li><svg width="10" height="10" viewBox="0 0 10 10"></svg>ABN 1290475566310</li>
    </ul>
    <div class="back-panel__band"></div>
  </div>
</section>

</body>
</html>
```